Need Business cards

Im a new realtor and already have a logo. I would like to purchase a Business card design that catches customer's attention, its creative, and modern.

Marisol Vandera
Realtor ®
(555) 214 7730
marisolvndrealtor@brightmailbox.com

Target Market(s)

investors, buyers and seller, property management

Industry/Entity Type

real estate,

Contact Information for Business Card

Marisol Vandera

Requirements
Must have
• BOTH LOGOS, WOULD LIKE TO SEE WITH DIFFERENT OPTIONS WITH EITHER PICTURE

```html
<!DOCTYPE html>
<html lang="en">
<head>
<meta charset="utf-8">
<title>Marisol Vandera – Business Cards</title>
<link href="https://fonts.googleapis.com/css2?family=Montserrat:wght@400;500;600;700&display=swap" rel="stylesheet">
<style>
  :root {
    --backdrop: #dcdcdc;
    --card: #1c1c1c;
    --gold: #c9a735;
    --gold-light: #e2c54a;
    --gold-dark: #a8852a;
    --white: #f4f4f4;
    --photo-top: #e9e6e4;
    --photo-bottom: #b98f63;
  }
  * { margin: 0; padding: 0; box-sizing: border-box; }
  html, body { width: 1200px; height: 1101px; overflow: hidden; }
  body {
    background: var(--backdrop);
    font-family: "Montserrat", sans-serif;
    position: relative;
  }
  .card {
    position: absolute;
    width: 302px;
    height: 530px;
    background: var(--card);
  }
  .card--front { left: 246px; top: 268px; }
  .card--back { left: 642px; top: 267px; height: 528px; }

  .portrait-ring {
    position: absolute;
    left: 52px; top: 57px;
    width: 200px; height: 200px;
    border: 2px solid var(--gold);
    border-radius: 50%;
  }
  .portrait {
    position: absolute;
    left: 6px; top: 6px;
    width: 184px; height: 184px;
    border-radius: 50%;
    background: radial-gradient(circle at 50% 40%, var(--photo-top) 0%, #d8c1a6 45%, var(--photo-bottom) 100%);
  }
  .agent-name {
    position: absolute;
    top: 286px; left: 0; width: 100%;
    text-align: center;
    color: var(--white);
    font-weight: 700;
    font-size: 22px;
  }
  .agent-title {
    position: absolute;
    top: 313px; left: 0; width: 100%;
    text-align: center;
    color: var(--white);
    font-weight: 500;
    font-size: 19px;
  }
  .contact-divider {
    position: absolute;
    left: 54px; top: 356px;
  }
  .contact-line {
    position: absolute;
    left: 0; width: 100%;
    text-align: center;
    color: var(--white);
    font-size: 14.5px;
    font-weight: 400;
  }
  .contact-line--phone { top: 401px; }
  .contact-line--email { top: 427px; font-size: 12.5px; }
  .brokerage-band {
    position: absolute;
    left: 0; top: 479px;
    width: 100%; height: 35px;
    background: linear-gradient(90deg, var(--gold-light), var(--gold) 55%, var(--gold-dark));
    display: flex; align-items: center; justify-content: center;
  }
  .brokerage-name {
    color: #1f1f1f;
    font-weight: 700;
    font-size: 15px;
    letter-spacing: 1px;
    text-transform: uppercase;
  }

  .brand-mark {
    position: absolute;
    left: 0; top: 196px; width: 100%;
    display: flex; justify-content: center;
  }
  .brand-square {
    width: 70px; height: 70px;
    border: 3px solid var(--gold);
  }
  .brand-name {
    position: absolute;
    top: 317px; left: 0; width: 100%;
    text-align: center;
    color: var(--gold);
    font-weight: 600;
    font-size: 15.5px;
    letter-spacing: 0.3px;
    text-transform: uppercase;
  }
  .brand-tagline {
    position: absolute;
    top: 336px; left: 0; width: 100%;
    display: flex; align-items: center; justify-content: center; gap: 5px;
    color: var(--gold);
    font-weight: 500;
    font-size: 11.5px;
    text-transform: uppercase;
  }
  .brand-tagline::before, .brand-tagline::after {
    content: ""; width: 46px; height: 1px; background: var(--gold);
  }
</style>
</head>
<body>
  <section class="card card--front">
    <div class="portrait-ring">
      <div class="portrait" role="img" aria-label="Headshot portrait of the realtor"></div>
    </div>
    <h1 class="agent-name">Marisol Vandera</h1>
    <p class="agent-title">Realtor ®</p>
    <svg class="contact-divider" width="194" height="24" viewBox="0 0 194 24" aria-hidden="true">
      <line x1="0" y1="12" x2="63" y2="12" stroke="#c9a735" stroke-width="1.5"/>
      <line x1="132" y1="12" x2="194" y2="12" stroke="#c9a735" stroke-width="1.5"/>
      <circle cx="80" cy="12" r="11" fill="#c9a735"/>
      <path d="M75.5 7.5c.6-.6 1.4-.5 1.8.1l1.2 1.8c.3.5.2 1.1-.2 1.5l-.7.6c.6 1.3 1.6 2.3 2.9 2.9l.6-.7c.4-.4 1-.5 1.5-.2l1.8 1.2c.6.4.7 1.2.1 1.8l-.8.8c-.7.7-1.8.9-2.7.4-2.5-1.2-4.6-3.3-5.8-5.8-.5-.9-.3-2 .4-2.7z" fill="#1c1c1c"/>
      <circle cx="115" cy="12" r="11" fill="#c9a735"/>
      <rect x="109" y="8" width="12" height="8.5" rx="1" fill="#1c1c1c"/>
      <path d="M109.5 8.5l5.5 4.3 5.5-4.3" fill="none" stroke="#c9a735" stroke-width="1.1"/>
    </svg>
    <p class="contact-line contact-line--phone">(555) 214 7730</p>
    <p class="contact-line contact-line--email">marisolvndrealtor@brightmailbox.com</p>
    <div class="brokerage-band">
      <span class="brokerage-name">Northgate Realty</span>
    </div>
  </section>

  <section class="card card--back">
    <div class="brand-mark"><div class="brand-square"></div></div>
    <p class="brand-name">Marisol Vandera</p>
    <p class="brand-tagline">Realtor</p>
  </section>
</body>
</html>
```